Solar Billboard Design

We require a billboard 24ftx10ft in size for our solar company.
Artwork Requirement’s:
• Sent on PDF file
• At least 300 dpi
• Scaled to 25% of banner size (24ft x 10ft)
• Please allow at least 40mm space from the artwork edge to allow for any hems and eyelets. This will ensure any important text/images are not cropped/overlapped.
The billboard must have on it:
Solar & Battery Packages
From £8750
In Stock Now!
brightfieldpower.co.uk (must stand out)
________________________
I have attached our logo and some images. I'm not sure if they are good enough quality so you may need to use a stock image.
Kind regards,
Marcus
Target Market(s)
Men & Women aged 35-70, homeowners
Industry/Entity Type
Solar / Construction
Look and feel
Each slider illustrates characteristics of the customer's brand and the style your logo design should communicate.

```html
<!DOCTYPE html>
<html lang="en">
<head>
<meta charset="UTF-8">
<title>Brightfield Energy Group – Solar &amp; Battery Billboard</title>
<link rel="stylesheet" href="https://fonts.googleapis.com/css2?family=Bebas+Neue&family=Montserrat:wght@600&display=swap">
<style>
  :root {
    --brand-green: #2ecc5f;
    --ink-dark: #454344;
    --ink-black: #141414;
    --paper: #ffffff;
    --frame-grey: #9a9a9a;
    --frame-light: #d6d6d6;
    --photo-sky: #aebfcf;
    --photo-hills: #4f6a52;
    --photo-roof: #3a4152;
    --photo-wall: #c9ccd4;
  }
  html, body {
    margin: 0;
    padding: 0;
    overflow: hidden;
    background: var(--paper);
  }
  .billboard {
    position: relative;
    width: 1200px;
    height: 508px;
    background: var(--paper);
    overflow: hidden;
    font-family: "Bebas Neue", "Arial Narrow", sans-serif;
  }
  .billboard__frame {
    position: absolute;
    left: 17px;
    top: 11px;
    width: 1169px;
    height: 487px;
    border: 1px solid var(--frame-grey);
    box-sizing: border-box;
    pointer-events: none;
  }
  .billboard__safe-line {
    position: absolute;
    left: 25px;
    top: 19px;
    width: 1153px;
    height: 471px;
    border: 1px solid var(--frame-light);
    box-sizing: border-box;
    pointer-events: none;
  }
  .hero-photo {
    position: absolute;
    left: 17px;
    top: 11px;
    width: 599px;
    height: 487px;
    background:
      linear-gradient(180deg,
        var(--photo-sky) 0%,
        var(--photo-hills) 18%,
        var(--photo-roof) 32%,
        var(--photo-roof) 62%,
        var(--photo-wall) 78%,
        #8a8f97 100%);
  }
  .corner-accent {
    position: absolute;
    left: 17px;
    top: 411px;
    width: 33px;
    height: 87px;
    background: var(--brand-green);
  }
  .corner-tab {
    position: absolute;
    left: 1153px;
    top: 11px;
    width: 33px;
    height: 106px;
    background: var(--ink-dark);
  }
  .brand-name {
    position: absolute;
    left: 806px;
    top: 48px;
    display: flex;
    align-items: center;
    gap: 16px;
  }
  .brand-name__mark {
    width: 40px;
    height: 40px;
    background: var(--brand-green);
  }
  .brand-name__text {
    font-family: "Montserrat", Arial, sans-serif;
    font-weight: 600;
    font-size: 17px;
    line-height: 22px;
    letter-spacing: 3.5px;
    color: var(--ink-dark);
    text-transform: uppercase;
  }
  .headline {
    position: absolute;
    left: 616px;
    width: 571px;
    top: 134px;
    margin: 0;
    text-align: center;
    font-weight: 400;
    font-size: 80px;
    line-height: 72px;
    color: var(--ink-dark);
  }
  .price-tag {
    position: absolute;
    left: 730px;
    top: 285px;
    width: 333px;
    height: 80px;
    background: var(--brand-green);
    color: var(--paper);
    font-size: 70px;
    line-height: 80px;
    text-align: center;
    padding-top: 4px;
    box-sizing: border-box;
  }
  .stock-note {
    position: absolute;
    left: 616px;
    width: 571px;
    top: 370px;
    margin: 0;
    text-align: center;
    font-size: 34px;
    line-height: 38px;
    letter-spacing: 1px;
    color: var(--ink-dark);
    text-transform: uppercase;
  }
  .web-band {
    position: absolute;
    left: 616px;
    top: 411px;
    width: 571px;
    height: 87px;
    background: var(--brand-green);
    color: var(--ink-black);
    font-size: 52px;
    line-height: 87px;
    text-align: center;
    padding-top: 3px;
    box-sizing: border-box;
    text-transform: uppercase;
  }
</style>
</head>
<body>
  <main class="billboard">
    <div class="hero-photo" role="img" aria-label="Aerial photo of a grey house with solar panels across its tiled roof, green hills and fields behind"></div>
    <div class="corner-accent"></div>
    <div class="corner-tab"></div>

    <div class="brand-name">
      <span class="brand-name__mark"></span>
      <span class="brand-name__text">Brightfield<br>Energy<br>Group</span>
    </div>

    <h1 class="headline">Solar &amp; Battery<br>Packages</h1>

    <div class="price-tag">From £8750</div>

    <p class="stock-note">In Stock Now!</p>

    <div class="web-band">brightfieldpower.co.uk</div>

    <div class="billboard__safe-line"></div>
    <div class="billboard__frame"></div>
  </main>
</body>
</html>
```